Verindo Living- Hang tags for Modern Handmade Home Decor products

We need to design some hang tags to use for our products, we want double tags, meaning two tags that go together on one string, two different and coordinating sizes and shapes. We have a logo, what we need is the artwork for these two tags to take to print. One tag will have the logo on one side and company information on the other, the second tag will be for product information. For example, we specialize in handmade pieces from Latin America, on the product tag I want space to write the product info but also a line for what country it's from and what community created it. I'm attaching an image of the shapes of tags that I like, along with a copy of our logo. On the larger company tag I'd like our logo in the center and a color block stripe of the yellow color of our logo at the bottom, on the flip side there will just be text, sort of our company motto. On the narrower longer product info tag I'd like a small logo at the bottom end and space for product information to be written in by hand and on the flip side of this one lines for what country it's from, what community created it and care instructions, again, all information that we will write in by hand. Please let me know if you have questions.

Target Market(s)

Design savvy, house proud, well educated people who travel and appreciate art.

Font styles to use
Sans Serif

Requirements
Must have
• I want it to look graphic, sophisticated and modern. I want to be very legible and clean.
Nice to have
• Clarity, easy to read, and maybe a bit of whimsy or lightheartedness.
Should not have
• Nothing that feels "ethnic" or "crafty:, even though our products are handmade in Latin America they are contemporary and sophisticated, not stereotypical.

```html
<!DOCTYPE html>
<html lang="en">
<head>
<meta charset="utf-8">
<title>Verindo Living — Hang Tags</title>
<link rel="stylesheet" href="https://fonts.googleapis.com/css2?family=Quicksand:wght@500&family=Montserrat:wght@500;600&display=swap">
<style>
  :root {
    --paper: #f4f4f4;
    --kraft: #cdb087;
    --kraft-light: #d6bb93;
    --kraft-dark: #c2a47a;
    --brand-yellow: #fdd318;
    --ink: #1a1a1a;
    --white: #ffffff;
    --eyelet: #d9d9d9;
  }
  * { box-sizing: border-box; margin: 0; padding: 0; }
  html, body { width: 1200px; height: 1000px; overflow: hidden; }
  body { background: var(--paper); position: relative; font-family: "Montserrat", sans-serif; }

  .tag { position: absolute; left: 0; top: 0; width: 1200px; height: 1000px; }
  .kraft-card {
    position: absolute;
    background: linear-gradient(160deg, var(--kraft-light), var(--kraft) 55%, var(--kraft-dark));
    border-radius: 28px;
    box-shadow: 0 2px 6px rgba(0,0,0,0.25);
  }
  .yellow-card {
    position: absolute;
    background: var(--brand-yellow);
    border-radius: 24px;
    box-shadow: 0 2px 6px rgba(0,0,0,0.3);
  }
  .eyelet {
    position: absolute;
    z-index: 2;
    width: 30px; height: 30px;
    border-radius: 50%;
    border: 4px solid var(--eyelet);
    background: var(--white);
    transform: translate(-50%, -50%);
  }
  .brand-name {
    position: absolute;
    left: 0; right: 0;
    text-align: center;
    font-family: "Quicksand", sans-serif;
    font-weight: 500;
    color: var(--white);
    line-height: 1;
    white-space: nowrap;
  }
  .accent-dot {
    position: absolute;
    border-radius: 50%;
    background: var(--brand-yellow);
  }

  /* Company tag */
  .company-tag .kraft-card { left: 125px; top: 177px; width: 437px; height: 633px; }
  .company-tag .yellow-card { left: 130px; top: 175px; width: 338px; height: 537px; }
  .company-tag .eyelet { left: 184px; top: 36px; }
  .company-tag .brand-mark {
    position: absolute; left: 129px; top: 150px;
    width: 80px; height: 80px; border-radius: 50%; background: var(--ink);
  }
  .company-tag .brand-name { top: 322px; font-size: 60px; }
  .company-tag .web-address {
    position: absolute; left: 0; right: 0; top: 391px;
    text-align: center; font-size: 13px; font-weight: 600;
    letter-spacing: 2.6px; color: var(--ink); white-space: nowrap;
  }
  .company-tag .origin {
    position: absolute; left: 160px; top: 755px;
    font-size: 26px; font-weight: 500; letter-spacing: 3.5px; line-height: 1;
    color: var(--ink); white-space: nowrap;
  }
  .company-tag .accent-dot { left: 484px; top: 752px; width: 30px; height: 30px; }

  /* Product tag */
  .product-tag .kraft-card { left: 745px; top: 93px; width: 338px; height: 817px; }
  .product-tag .yellow-card { left: 733px; top: 95px; width: 292px; height: 613px; }
  .product-tag .eyelet { left: 147px; top: 29px; }
  .product-tag .ornament-area {
    position: absolute; left: 42px; top: 25px; width: 190px; height: 520px;
    border-radius: 90px 90px 70px 40px;
    background: linear-gradient(180deg, rgba(26,26,26,0.55), rgba(26,26,26,0.8));
  }
  .product-tag .brand-name { top: 563px; font-size: 40px; }
  .write-in-lines { position: absolute; left: 775px; top: 752px; list-style: none; }
  .write-in-lines li { height: 25.6px; border-top: 2px solid var(--ink); width: 270px; }
  .write-in-lines li.short { width: 200px; }
  .product-tag .accent-dot { left: 1005px; top: 834px; width: 34px; height: 34px; }
</style>
</head>
<body>

  <section class="tag company-tag" aria-label="Company hang tag">
    <div class="kraft-card"></div>
    <div class="yellow-card">
      <span class="eyelet"></span>
      <span class="brand-mark"></span>
      <p class="brand-name">verindo</p>
      <p class="web-address">www.verindoliving.com</p>
    </div>
    <p class="origin">MADE IN USA</p>
    <span class="accent-dot"></span>
  </section>

  <section class="tag product-tag" aria-label="Product information hang tag">
    <div class="kraft-card"></div>
    <div class="yellow-card">
      <span class="eyelet"></span>
      <div class="ornament-area" role="img" aria-label="Black flowing scroll ornament running down the tag"></div>
      <p class="brand-name">verindo</p>
    </div>
    <ul class="write-in-lines" aria-label="Lines for handwritten product information">
      <li></li><li></li><li></li>
      <li class="short"></li><li class="short"></li><li class="short"></li>
    </ul>
    <span class="accent-dot"></span>
  </section>

</body>
</html>
```